Oil and Gas Company: Letterhead Design

In short we need a professional company letterhead designed for our Oil and Gas company.

We would like to keep the design simple and professional. Letterhead to include the company logo and color scheme, front page and continuation pages.

For reference, see attached logo below with our company logo and color scheme.

Target Market(s)

Oil & Gas Market

Industry/Entity Type

Oil And Gas

Font styles to use
Sans Serif

Requirements
Must have
• Letterhead must contain a front page & continuation page.
• Must be simple and professional in design.
• Follow our logo and color scheme.
Nice to have
• I would like to have the logo embedded in the bottom right hand portion of the page to provide some depth into the letterhead.

```html
<!DOCTYPE html>
<html lang="en">
<head>
<meta charset="utf-8">
<title>Ridgeline Energy Services – Letterhead</title>
<link href="https://fonts.googleapis.com/css2?family=Arimo:wght@400;500&family=Source+Sans+3:wght@400&display=swap" rel="stylesheet">
<style>
  :root {
    --backdrop: #5b3a22;
    --paper: #ffffff;
    --brand-blue: #135ca8;
    --brand-red: #e1232e;
    --ink: #1d2433;
    --rule: #d6d9de;
    --caption: #ffffff;
  }
  * { margin: 0; padding: 0; box-sizing: border-box; }
  html, body {
    width: 1200px;
    height: 830px;
    overflow: hidden;
    background: var(--backdrop);
  }
  .spread {
    position: relative;
    width: 1200px;
    height: 830px;
  }
  .sheet {
    position: absolute;
    top: 54px;
    width: 531px;
    height: 687px;
    background: var(--paper);
    box-shadow: 0 2px 8px rgba(0,0,0,0.35);
    font-family: "Arimo", Arial, sans-serif;
    color: var(--ink);
  }
  .sheet--front { left: 69px; }
  .sheet--continuation { left: 614px; }

  .brand {
    position: absolute;
    left: 13px;
    top: 28px;
    width: 80px;
    display: flex;
    flex-direction: column;
    align-items: center;
  }
  .brand__dot {
    width: 22px;
    height: 22px;
    border-radius: 50%;
    background: var(--brand-blue);
    margin-bottom: 14px;
  }
  .brand__name {
    font-weight: 500;
    font-size: 8px;
    line-height: 9px;
    letter-spacing: 0.3px;
    text-align: center;
    color: var(--ink);
    white-space: nowrap;
  }

  .contact {
    position: absolute;
    left: 348px;
    top: 24px;
    height: 62px;
    padding-left: 7px;
    border-left: 1px solid var(--rule);
    list-style: none;
  }
  .contact__item {
    display: flex;
    align-items: center;
    height: 16px;
    font-size: 8.6px;
    color: var(--ink);
    white-space: nowrap;
  }
  .contact__icon {
    width: 10px;
    height: 10px;
    margin-right: 6px;
    flex: none;
  }

  .address {
    position: absolute;
    left: 17px;
    top: 643px;
    display: flex;
    align-items: center;
    font-size: 10.5px;
    color: var(--ink);
  }
  .address__icon {
    width: 9px;
    height: 12px;
    margin-right: 6px;
  }

  .footer-band {
    position: absolute;
    left: 0;
    bottom: 0;
    width: 531px;
    height: 39px;
    display: block;
  }

  .sheet-label {
    position: absolute;
    font-family: "Source Sans 3", "Myriad Pro", sans-serif;
    font-size: 29px;
    color: var(--caption);
    transform: translateX(-50%);
  }
  .sheet-label--front { left: 255px; top: 756px; }
  .sheet-label--continuation { left: 852px; top: 748px; }
</style>
</head>
<body>
<main class="spread">

  <section class="sheet sheet--front" aria-label="Letterhead front page">
    <header>
      <div class="brand">
        <span class="brand__dot"></span>
        <span class="brand__name">RIDGELINE<br>ENERGY SERVICES</span>
      </div>
      <ul class="contact">
        <li class="contact__item">
          <svg class="contact__icon" viewBox="0 0 10 10"><circle cx="5" cy="5" r="4.3" fill="none" stroke="var(--brand-blue)" stroke-width="0.9"/><path d="M3.6 2.6 L4.6 2.4 L5 3.8 L4.3 4.3 C4.6 5.2 5 5.7 5.8 6.1 L6.3 5.4 L7.6 5.9 L7.4 6.9 C5.2 7.2 3.1 4.9 3.6 2.6Z" fill="var(--brand-blue)"/></svg>
          123-456-7890
        </li>
        <li class="contact__item">
          <svg class="contact__icon" viewBox="0 0 10 10"><rect x="2.6" y="0.5" width="4.8" height="9" rx="0.8" fill="var(--brand-blue)"/><rect x="3.3" y="1.5" width="3.4" height="4" fill="#fff"/><rect x="3.3" y="6.4" width="3.4" height="2.3" fill="#9fbde0"/></svg>
          123-456-7890
        </li>
        <li class="contact__item">
          <svg class="contact__icon" viewBox="0 0 10 10"><rect x="0.5" y="2" width="9" height="6" fill="var(--brand-blue)"/><path d="M0.8 2.3 L5 5.5 L9.2 2.3" fill="none" stroke="#fff" stroke-width="0.8"/></svg>
          inquiry@ridgelineenergyservices.com
        </li>
        <li class="contact__item">
          <svg class="contact__icon" viewBox="0 0 10 10" fill="none" stroke="var(--brand-blue)" stroke-width="0.8"><circle cx="5" cy="5" r="4.2"/><ellipse cx="5" cy="5" rx="1.9" ry="4.2"/><path d="M0.8 5 H9.2 M1.5 2.9 H8.5 M1.5 7.1 H8.5"/></svg>
          www.ridgelineenergyservices.com
        </li>
      </ul>
    </header>

    <footer>
      <p class="address">
        <svg class="address__icon" viewBox="0 0 9 12"><path d="M4.5 0.5 C2.3 0.5 0.8 2 0.8 4 C0.8 6.6 4.5 11.5 4.5 11.5 C4.5 11.5 8.2 6.6 8.2 4 C8.2 2 6.7 0.5 4.5 0.5Z" fill="var(--brand-blue)"/><circle cx="4.5" cy="4" r="1.4" fill="#fff"/></svg>
        Street Name, City Name, State Zipcode
      </p>
      <svg class="footer-band" viewBox="0 0 531 39" aria-hidden="true">
        <path d="M0 27 H300 C312 27 312 2 338 2 H531 V39 H0 Z" fill="var(--brand-blue)"/>
        <path d="M0 16 H300 C308 16 309 24 300 24 H0 Z" fill="var(--brand-red)"/>
        <path d="M0 26 H298 C309 26 313 14 318 9" fill="none" stroke="#fff" stroke-width="1.6"/>
      </svg>
    </footer>
  </section>

  <section class="sheet sheet--continuation" aria-label="Letterhead continuation page">
    <footer>
      <p class="address">
        <svg class="address__icon" viewBox="0 0 9 12"><path d="M4.5 0.5 C2.3 0.5 0.8 2 0.8 4 C0.8 6.6 4.5 11.5 4.5 11.5 C4.5 11.5 8.2 6.6 8.2 4 C8.2 2 6.7 0.5 4.5 0.5Z" fill="var(--brand-blue)"/><circle cx="4.5" cy="4" r="1.4" fill="#fff"/></svg>
        Street Name, City Name, State Zipcode
      </p>
      <svg class="footer-band" viewBox="0 0 531 39" aria-hidden="true">
        <path d="M0 27 H300 C312 27 312 2 338 2 H531 V39 H0 Z" fill="var(--brand-blue)"/>
        <path d="M0 16 H300 C308 16 309 24 300 24 H0 Z" fill="var(--brand-red)"/>
        <path d="M0 26 H298 C309 26 313 14 318 9" fill="none" stroke="#fff" stroke-width="1.6"/>
      </svg>
    </footer>
  </section>

  <p class="sheet-label sheet-label--front">Page 1</p>
  <p class="sheet-label sheet-label--continuation">Page 2</p>

</main>
</body>
</html>
```